Veteran owned/staffed Organization that hires Veterans into Ironworking

Please see attached documents for all details and info.
We want a tri-fold brochure to use as a recruiting tool.
Our slogan is:
"Revolutionizing the skilled workforce, one Veteran at a time"
Veteran Apprenticeship Program in Ironworking
Skills/Traits: Welding, bolting, rigging, connecting
Teamwork, camaraderie, TK Grant, Skilled Labor, Career, Community service
OJT, Apprenticeship, Career
Due to the large number of retirees from the baby boomer generation, ironworkers are in high demand. In Texas, the construction industry is on the rise and due to our training regiment, an average of 40 hrs/wk are worked. Our apprenticeship program follows the PLWTO curriculum and at the end of the 3-year course involving classroom learning, OJT and practical application the apprentice achieves journeymen status in ironworking. Journeyman status opens the door to possible postions like foremen, crane operators and project managers. Ironworkers perform their duties on steel structures that provide a skeleton for commercial buildings like hospitals, schools and skyscrapers. Some of the key skilled trades of ironworking are welding, rigging, bolting and connecting.
All Things Veterans
Camaraderie and Culture
-Veteran owned and majority staffed organization who are committed to the mission of providing opportunitites to Veterans
-Graduation celebration after completion of initial training period, holiday parties and get togethers at HQBs
-Work with other Veterans and always have your teammate’s six
-We’re building America, one Veteran career at a time
Professional Support
BDR is committed to providing Veterans with supportive services designed to assist you and your families in the following areas:
Financial, family and work-related support.
Community Service
Disaster Response
Louisiana Flooding - Sept 2016
As the 15th anniversery of 9/11 approached BDR worked to find a volunteer opportunity. An ambitious plan was formed to respond to the devastating 1000-year flood event in Baton Rouge. With little time for planning, BDR organized all the tools and supplies necessary to take 24 Veterans to assist a community in extreme poverty. The team gutted the homes of nine residents which included: single mothers, handicapped elderaly and a Korean War Veterans
Hurricane Orlend - Oct 2016
In a period of 24 hours BDR mobilized 16 Veterans with the supplies neccessary to be 100% self-reliant. The team arrived in Holly Hill, SC 8 hours after Hurrican Orlend made landfall. During a period of 2 days, BDR provided over 5,000 meals, distributed 40,000 bottles of water and removed nearly 100 trees.

Target Market(s)

Veterans who are interested in becoming Ironworkers. Usually under the age of 40, have served in the military and are in the Texas area.

Industry/Entity Type

Construction

Font styles to use
Other font styles liked:
• Microgramma in some places (Logo font) and Serif type font for the bulk

Requirements
Must have
• The colors and logo mentioned in the template guidelines document.
• The slogan
• "Revolutionizing the skilled workforce, one Veteran at a time"
Nice to have
• Some charts and graphs if possible?

```html
<!DOCTYPE html>
<html lang="en">
<head>
<meta charset="utf-8">
<title>BDR Tri-fold Brochure – Outer Spread</title>
<link href="https://fonts.googleapis.com/css2?family=Lato:wght@400;700&family=Oswald:wght@400;600&display=swap" rel="stylesheet">
<style>
  :root {
    --navy: #1e3552;
    --navy-deep: #172a42;
    --gold: #d99a45;
    --gold-light: #ebb56c;
    --gold-dark: #b87a33;
    --white: #ffffff;
    --page: #e6e6e6;
    --steel-1: #5b7a99;
    --steel-2: #2c4661;
  }
  * { box-sizing: border-box; margin: 0; padding: 0; }
  html, body { width: 1200px; height: 948px; overflow: hidden; background: var(--page); }
  .spread {
    position: absolute; left: 45px; top: 44px;
    width: 1110px; height: 860px;
    display: flex;
    box-shadow: 0 6px 24px rgba(0,0,0,.25);
  }
  .panel { position: relative; width: 370px; height: 860px; overflow: hidden; }
  .panel svg.shape { position: absolute; inset: 0; }

  /* Panel 1 – program info */
  .panel-info { background: var(--navy); }
  .info-title {
    position: absolute; left: 26px; top: 40px;
    font: 600 25px/1 "Oswald", sans-serif; color: var(--gold);
  }
  .info-body {
    position: absolute; left: 26px; top: 88px; width: 318px;
    font: 400 12.6px/19px "Lato", sans-serif; color: var(--white);
    text-align: justify;
  }

  /* Panel 2 – contact */
  .panel-contact { background: linear-gradient(180deg, var(--gold-light), var(--gold-dark)); }
  .contact {
    position: absolute; left: 0; top: 642px; width: 370px; text-align: center;
    font: 400 14px/22px "Lato", sans-serif; color: var(--navy);
  }
  .contact .org { font-weight: 700; font-size: 16px; margin-bottom: 4px; }

  /* Logo stand-in */
  .brand {
    position: absolute; left: 0; width: 370px;
    display: flex; justify-content: center; align-items: center; gap: 10px;
  }
  .brand-mark { width: 16px; height: 16px; background: var(--gold); }
  .brand-name { font: 600 44px/1 "Oswald", sans-serif; color: var(--gold); letter-spacing: 2px; }

  /* Web pill */
  .web-pill {
    position: absolute; left: 50%; transform: translateX(-50%);
    width: 210px; height: 24px; border-radius: 12px;
    background: var(--navy); color: var(--white);
    font: 400 12px/24px "Lato", sans-serif; letter-spacing: 3px; text-align: center;
  }

  /* Panel 3 – cover */
  .panel-cover { background: var(--white); }
  .slogan { position: absolute; left: 0; top: 668px; width: 370px; text-align: center; color: var(--navy); }
  .slogan-lead { font: 600 47px/1 "Oswald", sans-serif; color: var(--gold); letter-spacing: 1px; }
  .slogan-mid { font: 400 25px/1.2 "Oswald", sans-serif; margin-top: 4px; }
  .slogan-end { font: 600 23px/1.15 "Oswald", sans-serif; font-style: italic; letter-spacing: 1px; }
</style>
</head>
<body>
<main class="spread">

  <section class="panel panel-info">
    <h2 class="info-title">OJT, Apprenticeship, Career</h2>
    <p class="info-body">Due to the large number of retirees from the baby boomer generation, ironworkers are in high demand. In Texas, the construction industry is on the rise and due to our training regiment, an average of 40 hrs/wk are worked. Our apprenticeship program follows the PLWTO curriculum and at the end of the 3-year course involving classroom learning, OJT and practical application the apprentice achieves journeymen status in ironworking. Journeyman status opens the door to possible postions like foremen, crane operators and project managers. Ironworkers perform their duties on steel structures that provide a skeleton for commercial buildings like hospitals, schools and skyscrapers. Some of the key skilled trades of ironworking are welding, rigging, bolting and connecting.</p>
    <svg class="shape" width="370" height="860" viewBox="0 0 370 860">
      <defs>
        <linearGradient id="ironwork-fill" x1="0" y1="0" x2="1" y2="1">
          <stop offset="0" stop-color="#7d8fa3"/>
          <stop offset=".55" stop-color="#c4562e"/>
          <stop offset="1" stop-color="#4a4f57"/>
        </linearGradient>
      </defs>
      <polygon points="0,745 370,700 370,860 0,860" fill="var(--white)"/>
      <polygon points="180,402 335,492 335,672 180,762 25,672 25,492" fill="none" stroke="var(--gold)" stroke-width="3"/>
      <polygon points="180,412 326,497 326,667 180,752 34,667 34,497" fill="url(#ironwork-fill)" role="img" aria-label="Photo: ironworkers rigging a large steel component on a construction site"/>
    </svg>
  </section>

  <section class="panel panel-contact">
    <svg class="shape" width="370" height="860" viewBox="0 0 370 860">
      <defs>
        <linearGradient id="steel-fill" x1="0" y1="0" x2="0" y2="1">
          <stop offset="0" stop-color="var(--steel-1)"/>
          <stop offset="1" stop-color="var(--steel-2)"/>
        </linearGradient>
      </defs>
      <rect x="0" y="0" width="370" height="430" fill="url(#steel-fill)" role="img" aria-label="Photo: workers on a steel building frame, tinted blue"/>
      <polygon points="0,380 370,380 370,520 185,600 0,520" fill="var(--navy)"/>
    </svg>
    <div class="brand" style="top:448px"><span class="brand-mark"></span><span class="brand-name">BDR</span></div>
    <address class="contact">
      <div class="org">Bastion Development Resources, Inc.</div>
      <div>P.O Box 412</div>
      <div>Kestrel, TX 75510-0412</div>
      <div style="margin-top:6px">Recruiting@BDRTexas.com</div>
    </address>
    <div class="web-pill" style="top:770px">www.bdrtexas.com</div>
  </section>

  <section class="panel panel-cover">
    <svg class="shape" width="370" height="860" viewBox="0 0 370 860">
      <defs>
        <linearGradient id="welder-fill" x1="0" y1="0" x2="1" y2="1">
          <stop offset="0" stop-color="#6b5a45"/>
          <stop offset=".5" stop-color="#b9a88a"/>
          <stop offset="1" stop-color="#4b3f33"/>
        </linearGradient>
      </defs>
      <polygon points="0,0 370,0 370,560 185,640 0,560" fill="var(--navy)"/>
      <polygon points="185,150 335,237 335,413 185,500 35,413 35,237" fill="none" stroke="var(--gold)" stroke-width="4"/>
      <polygon points="185,160 326,242 326,408 185,490 44,408 44,242" fill="url(#welder-fill)" role="img" aria-label="Photo: veteran welder in protective helmet and gloves at work"/>
    </svg>
    <div class="brand" style="top:60px"><span class="brand-mark"></span><span class="brand-name">BDR</span></div>
    <div class="slogan">
      <div class="slogan-lead">REVOLUTIONIZING</div>
      <div class="slogan-mid">THE SKILLED WORKFORCE</div>
      <div class="slogan-end">ONE VETERAN AT A TIME</div>
    </div>
    <div class="web-pill" style="top:800px">www.bdrtexas.com</div>
  </section>

</main>
</body>
</html>
```